Tarrow Building Ventures needs a Business card design and logo

We Need a business card design and logo for a Building & Construction business based in Melbourne. We work in both the Domestic & Commercial sector. We specialize in all aspects of building including extensions, Renovations, and alterations. Construction Management, Project Management, And labour hire
Updates

Industry/Entity Type

Business

```html
<!DOCTYPE html>
<html lang="en">
<head>
<meta charset="utf-8">
<title>Tarrow Building Ventures – Business Card</title>
<link href="https://fonts.googleapis.com/css2?family=Roboto+Condensed:wght@400;500&family=Roboto:wght@400&display=swap" rel="stylesheet">
<style>
  :root {
    --page-bg: #e6e4e1;
    --card-bg: #f3f3f5;
    --card-fade: #e9e9ec;
    --teal: #14a99b;
    --gold: #d4a72c;
    --gold-dark: #b98f1c;
    --slate: #6f7073;
    --white: #ffffff;
  }
  html, body {
    margin: 0;
    padding: 0;
    width: 1200px;
    height: 900px;
    overflow: hidden;
    background: var(--page-bg);
  }
  .canvas {
    position: relative;
    width: 1200px;
    height: 900px;
  }
  .card {
    position: absolute;
    left: 150px;
    top: 175px;
    width: 900px;
    height: 550px;
    border-radius: 34px;
    overflow: hidden;
    background: linear-gradient(180deg, var(--card-bg) 0%, var(--card-fade) 45%, var(--card-bg) 70%);
    box-shadow: 0 10px 30px rgba(0,0,0,0.18);
  }
  .brand {
    position: absolute;
    top: 130px;
    left: 0;
    width: 100%;
    text-align: center;
  }
  .brand-name {
    margin: 0;
    font-family: "Roboto Condensed", sans-serif;
    font-weight: 500;
    font-size: 50px;
    letter-spacing: 0.5px;
    color: var(--gold);
    text-transform: uppercase;
    line-height: 1;
  }
  .brand-tagline {
    margin: 8px 0 0;
    font-family: "Roboto Condensed", sans-serif;
    font-weight: 400;
    font-size: 22px;
    color: var(--slate);
    text-transform: uppercase;
    line-height: 1;
  }
  .services {
    position: absolute;
    top: 318px;
    left: 0;
    width: 100%;
    margin: 0;
    padding: 0;
    list-style: none;
    display: flex;
    justify-content: center;
    font-family: "Roboto Condensed", sans-serif;
    font-size: 25px;
    color: var(--gold-dark);
  }
  .services li + li::before {
    content: "|";
    margin: 0 20px;
    color: var(--slate);
  }
  .contact-band {
    position: absolute;
    left: 0;
    bottom: 0;
    width: 100%;
    height: 142px;
    background: var(--teal);
    border-top: 7px solid var(--gold);
    display: flex;
    align-items: center;
  }
  .person-name {
    margin: 0 0 0 78px;
    font-family: "Roboto Condensed", sans-serif;
    font-weight: 500;
    font-size: 44px;
    color: var(--white);
    white-space: nowrap;
  }
  .contact-details {
    margin-left: 42px;
    font-family: "Roboto", sans-serif;
    font-size: 18px;
    color: var(--white);
    line-height: 1.35;
  }
  .contact-row span + span {
    margin-left: 34px;
  }
</style>
</head>
<body>
  <main class="canvas">
    <article class="card">
      <header class="brand">
        <h1 class="brand-name">Tarrow Building Ventures</h1>
        <p class="brand-tagline">Domestic and Commercial Builders</p>
      </header>

      <ul class="services">
        <li>Extentions</li>
        <li>Renovations</li>
        <li>Alterations</li>
        <li>Decks</li>
        <li>Pargolas</li>
      </ul>

      <footer class="contact-band">
        <h2 class="person-name">Dean Harlow</h2>
        <div class="contact-details">
          <div class="contact-row">
            <span>Mobile: 0400 555 018</span>
            <span>Office: (03) 9000 4172</span>
          </div>
          <div class="contact-row">
            <span>Email: info@tarrowbuildingventures.com</span>
          </div>
        </div>
      </footer>
    </article>
  </main>
</body>
</html>
```